Quellwind Gulfside LLC

we need a business card design

Industry/Entity Type

hvac

Contact Information for Business Card

my logo

Requirements
Must have
• my logo and same colors

```html
<!DOCTYPE html>
<html lang="en">
<head>
<meta charset="utf-8">
<title>Quellwind Gulfside LLC — Business Card</title>
<link rel="stylesheet" href="https://fonts.googleapis.com/css2?family=Montserrat:wght@400;500;700;800&display=swap">
<style>
  :root {
    --page-bg: #e9ebee;
    --card-white: #ffffff;
    --navy: #0a3b93;
    --navy-deep: #062c78;
    --cyan: #17b3e0;
    --orange: #f6b655;
    --ink: #2b2b2b;
    --rule: #8a8a8a;
  }
  * { box-sizing: border-box; margin: 0; padding: 0; }
  html, body {
    width: 1200px; height: 1200px; overflow: hidden;
    background: var(--page-bg);
    font-family: "Montserrat", sans-serif;
  }
  .sheet {
    position: relative; width: 1200px; height: 1200px;
    display: flex; flex-direction: column; align-items: center;
    justify-content: center; gap: 44px;
  }
  .card {
    position: relative; width: 940px; height: 520px;
    border-radius: 36px; overflow: hidden;
    box-shadow: 0 14px 30px rgba(0,0,0,.18);
  }

  /* Front */
  .card-front { background: var(--card-white); }
  .front-brand {
    position: absolute; left: 170px; top: 110px; width: 360px;
    display: flex; align-items: center; gap: 16px;
    color: var(--navy); font-weight: 800; font-size: 34px; line-height: 1.1;
  }
  .brand-dot {
    flex: none; width: 26px; height: 26px; border-radius: 50%;
    background: var(--orange);
  }
  .divider {
    position: absolute; left: 560px; top: 250px; width: 1.5px; height: 150px;
    background: var(--rule);
  }
  .person { position: absolute; left: 150px; top: 330px; }
  .person-name {
    color: var(--cyan); font-weight: 700; font-size: 44px; letter-spacing: .5px;
  }
  .person-title {
    color: var(--ink); font-weight: 400; font-size: 26px; margin-top: 2px;
  }
  .contact-list {
    position: absolute; left: 600px; top: 200px; list-style: none;
    color: var(--ink); font-size: 22px; font-weight: 400; line-height: 1.3;
  }
  .contact-item { display: flex; align-items: flex-start; gap: 12px; margin-bottom: 4px; }
  .contact-item svg { flex: none; width: 22px; height: 22px; margin-top: 3px; }
  .band { position: absolute; bottom: 0; height: 26px; }
  .band-cyan { left: 0; width: 580px; background: var(--cyan); }
  .band-orange { left: 590px; right: 0; background: var(--orange); height: 34px; }

  /* Back */
  .card-back {
    background: radial-gradient(ellipse at 45% 40%, var(--navy) 0%, var(--navy-deep) 100%);
    display: flex; align-items: center; justify-content: center;
  }
  .back-brand {
    display: flex; align-items: center; gap: 22px;
    color: var(--card-white); font-weight: 800; font-size: 50px; line-height: 1.1;
    max-width: 620px;
  }
  .back-brand .brand-dot { width: 40px; height: 40px; }
</style>
</head>
<body>
<main class="sheet">
  <section class="card card-front">
    <div class="front-brand"><span class="brand-dot"></span><span>Quellwind Gulfside LLC</span></div>
    <div class="divider"></div>
    <div class="person">
      <div class="person-name">FULL NAME</div>
      <div class="person-title">TITLE</div>
    </div>
    <ul class="contact-list">
      <li class="contact-item">
        <svg viewBox="0 0 24 24"><path fill="#17b3e0" d="M6.6 10.8a15 15 0 0 0 6.6 6.6l2.2-2.2c.3-.3.7-.4 1-.2 1.1.4 2.3.6 3.6.6.6 0 1 .4 1 1V20c0 .6-.4 1-1 1A17 17 0 0 1 3 4c0-.6.4-1 1-1h3.5c.6 0 1 .4 1 1 0 1.3.2 2.5.6 3.6.1.3 0 .7-.2 1z"/></svg>
        <span>(000) 000 0000</span>
      </li>
      <li class="contact-item">
        <svg viewBox="0 0 24 24"><path fill="#17b3e0" d="M2 5h20v14H2z"/><path fill="none" stroke="#fff" stroke-width="1.6" d="M2 5l10 8 10-8"/></svg>
        <span>email@company.com</span>
      </li>
      <li class="contact-item">
        <svg viewBox="0 0 24 24"><circle cx="12" cy="12" r="10" fill="none" stroke="#17b3e0" stroke-width="2"/><path fill="none" stroke="#17b3e0" stroke-width="1.5" d="M2 12h20M12 2c3 3 3 17 0 20M12 2c-3 3-3 17 0 20"/></svg>
        <span>www.company.com</span>
      </li>
      <li class="contact-item">
        <svg viewBox="0 0 24 24"><path fill="#17b3e0" d="M12 2a7 7 0 0 0-7 7c0 5 7 13 7 13s7-8 7-13a7 7 0 0 0-7-7zm0 9.5A2.5 2.5 0 1 1 12 6.5a2.5 2.5 0 0 1 0 5z"/></svg>
        <span>123 Name Street, 000<br>Your City, 00000-000</span>
      </li>
    </ul>
    <div class="band band-cyan"></div>
    <div class="band band-orange"></div>
  </section>

  <section class="card card-back">
    <div class="back-brand"><span class="brand-dot"></span><span>Quellwind Gulfside LLC</span></div>
  </section>
</main>
</body>
</html>
```